Pawlume Tonic - Functtional water for dogs. Brand new product

I have a design alreday. It needs an upgrade. I need it in two steps. One that sums everything in 5 pges and one as the one as sent as the longer brief. So one that is a full version and one summary. I want it to be rea professional for a presentation to investors, stores etc. Important to make the same thur out the presentation so it feels like it belongs together. High end business but still modern for a brand new unique product. The first product on the market is Morning Brinefix (the other 3 mighgt come later on). Its in Sweden we start like a city like stockholm. Important that its realistic. Not to dark. Again think towards high end investors.

Target Market(s)

The presentation is for investors och businesses. The product is for dogowners who keep their animals as family members, active people, city people, people who travel etc

Industry/Entity Type

Dogs och dog food and vitamins

Requirements
Must have
• High end but still modern and breathe a brand new product thats unique. For investors that will invest money in this project.

```html
<!DOCTYPE html>
<html lang="en">
<head>
<meta charset="utf-8">
<title>Why Now? – Pawlume Tonic</title>
<link rel="stylesheet" href="https://fonts.googleapis.com/css2?family=Poppins:wght@400;500;600;800&family=Outfit:wght@600;700&display=swap">
<style>
  :root {
    --backdrop: #373f4b;
    --slide-bg: #f3f4f6;
    --navy: #0a2e82;
    --sky: #93bbdf;
    --body-text: #4f5866;
    --chip-text: #555e6b;
    --white: #ffffff;
  }
  * { margin: 0; padding: 0; box-sizing: border-box; }
  html, body {
    width: 1200px; height: 1001px; overflow: hidden;
    background: var(--backdrop);
  }
  .slide {
    position: absolute; left: 0; top: 163px;
    width: 1200px; height: 675px;
    background: var(--slide-bg);
    overflow: hidden;
    font-family: "Poppins", sans-serif;
  }
  .accent-ring { position: absolute; left: 0; top: 0; width: 1200px; height: 675px; }
  .title {
    position: absolute; left: 88px; top: 98px;
    font-weight: 800; font-size: 51px; letter-spacing: -0.5px;
    color: var(--navy); line-height: 1.2;
  }
  .title-rule {
    position: absolute; left: 88px; top: 164px;
    width: 133px; height: 5px; background: var(--sky);
  }
  .lead, .intro {
    position: absolute; left: 88px; width: 540px;
    font-size: 17px; line-height: 24px; color: var(--body-text);
  }
  .lead { top: 221px; }
  .lead strong { color: var(--navy); font-weight: 600; }
  .intro { top: 376px; width: 530px; }
  .use-cases {
    position: absolute; left: 88px; top: 474px;
    display: grid; grid-template-columns: 256px 256px;
    column-gap: 16px; row-gap: 17px;
  }
  .chip {
    height: 44px; border: 2px solid var(--sky); border-radius: 9px;
    display: flex; align-items: center; gap: 14px; padding-left: 16px;
    font-size: 18.5px; font-weight: 500; color: var(--chip-text);
    letter-spacing: 0.3px;
  }
  .chip svg { width: 20px; height: 20px; flex: none; }
  .photo-dog {
    position: absolute; left: 677px; top: 89px;
    width: 423px; height: 586px;
    border-radius: 200px 200px 0 0;
    background: radial-gradient(ellipse at 50% 35%, #ffffff 0%, #e9edf3 45%, #b9c9e2 75%, #2c4f93 100%);
  }
  .quote {
    position: absolute; left: 635px; top: 468px;
    width: 519px; height: 122px;
    background: var(--navy); border-radius: 9px;
    padding: 16px 24px 0 35px;
    font-family: "Outfit", sans-serif; font-weight: 700;
    font-size: 28px; line-height: 30px; color: var(--white);
    letter-spacing: 0.2px;
  }
</style>
</head>
<body>
  <section class="slide">
    <svg class="accent-ring" viewBox="0 0 1200 675" aria-hidden="true">
      <circle cx="1086" cy="76" r="513" fill="none" stroke="#93bbdf" stroke-width="54"/>
    </svg>

    <h1 class="title">WHY NOW?</h1>
    <div class="title-rule"></div>

    <p class="lead">The global pet industry is rapidly evolving as owners increasingly treat their dogs as family members.Consumers already spend billions every year on premium nutrition, supplements and functional beverages for themselves, <strong>yet there is virtually no established hydration category for dogs.</strong></p>

    <p class="intro">Pawlume Tonic fills this gap with a product designed for real-life situations such as:</p>

    <div class="use-cases">
      <div class="chip">
        <svg viewBox="0 0 24 24"><path d="M13 2 4 14h7l-1 8 9-12h-7z" fill="#0a2e82"/></svg>
        Exercise &amp; Running
      </div>
      <div class="chip">
        <svg viewBox="0 0 24 24" fill="none" stroke="#0a2e82" stroke-width="1.8"><path d="M10 3a2 2 0 0 1 4 0v11a4 4 0 1 1-4 0z"/><circle cx="12" cy="17.5" r="1.6" fill="#0a2e82"/><circle cx="18" cy="4" r="1.4"/></svg>
        Warm Weather
      </div>
      <div class="chip">
        <svg viewBox="0 0 24 24"><path d="M21 16v-2l-8-5V3.5a1.5 1.5 0 0 0-3 0V9l-8 5v2l8-2.5V19l-2 1.5V22l3.5-1 3.5 1v-1.5L13 19v-5.5z" fill="#0a2e82" transform="rotate(90 12 12)"/></svg>
        Travel Stress
      </div>
      <div class="chip">
        <svg viewBox="0 0 24 24" fill="none" stroke="#0a2e82" stroke-width="2"><rect x="2.5" y="6" width="19" height="13" rx="2"/><path d="M12 9.5v6M9 12.5h6M6.5 6v13M17.5 6v13"/></svg>
        Fast Recovery
      </div>
    </div>

    <div class="photo-dog" role="img" aria-label="Photo of a smiling dalmatian dog with blue-tinted spots"></div>

    <blockquote class="quote">“A clear first-mover opportunity in an underserved, high-margin premium category.”</blockquote>
  </section>
</body>
</html>
```